Harbor Sprouts Star Agency Casting Flyer

I need two similar flyers to promote casting but minor differences in content. attached is my website, so I want it similar to my website. 1. Invite Military Parents to email atbecome a brat @Harbor Sprouts Star Agency dot comAsk them to email a child's name, parents' military branch, age of child, headshot, child's talent and charity work or interest to me to be invited to become a brat. Looking for brats that are not only talented but brats that desire to give back to society. Volunteerism is important to Harbor Sprouts Star Agency. Looking for talent ages 5 - 17 2. Flyer that invites military service member parents to casting on March 25 10 am- 2 pm. Ask them to rsvp at join the sprouts @harbor sprouts star agency dot com Ask them to email a child's name, parents' military branch, age of child, headshot, child's talent and charity work or interestlimited reservations. Looking for brats that are not only talented but have a heart for volunteerism. Sprouts pitch in is important to the mission of Harbor Sprouts Star Agency. Looking for talent ages 5 - 17
Updates

Project Deadline Extended Reason: Give designers more time to submit. This is a very important tool for my agency. Added Saturday, March 4, 2017

Target Market(s)

Military Parents looking to get their children into the entertainment industry.

Industry/Entity Type

Modeling Agency

Font styles to use
Sans Serif
Script

Colors
3277b5

Requirements
Must have
• Playful and fun.. needs to fit with my website.
Nice to have
• Same color blue as logo, very important. Similar flier but one has a specific date.. the other is to be used for media and to advertise.
Should not have
• none

```html
<!DOCTYPE html>
<html lang="en">
<head>
<meta charset="utf-8">
<title>Harbor Sprouts Star Agency – Casting Flyers</title>
<link rel="stylesheet" href="https://fonts.googleapis.com/css2?family=Montserrat:wght@400;500;600;700&family=Oswald:wght@500;700&display=swap">
<style>
  :root {
    --brand: #3277b5;
    --brand-deep: #1656a3;
    --brand-bright: #1f8fd6;
    --accent-sky: #1a9be0;
    --ink: #1a1a1a;
    --body: #3c3c3c;
    --board: #000000;
    --paper: #ffffff;
    --mist: #e4e6ea;
  }
  * { box-sizing: border-box; margin: 0; padding: 0; }
  html, body { width: 1200px; height: 960px; overflow: hidden; background: var(--board); }
  body { position: relative; font-family: "Montserrat", sans-serif; }

  .flyer { position: absolute; background: var(--paper); overflow: hidden; }
  .flyer-info { left: 63px; top: 114px; width: 588px; height: 762px; }
  .flyer-event { left: 683px; top: 239px; width: 455px; height: 637px; }

  .backdrop {
    position: absolute; inset: 0;
    background:
      radial-gradient(circle at 20% 12%, rgba(210,212,218,.7), transparent 35%),
      radial-gradient(circle at 80% 30%, rgba(215,217,222,.6), transparent 40%),
      linear-gradient(180deg, var(--mist) 0%, #f6f7f9 45%, var(--paper) 70%);
  }

  .photo {
    position: absolute; border-radius: 40px;
    background: linear-gradient(160deg, #d9533e 0%, #7b8fb8 45%, #6a4a3a 80%);
    opacity: .85;
  }
  .photo-girl { background: linear-gradient(170deg, #c9a57a 0%, #3ab0e0 35%, #5a3e2e 75%, #40b5e4 100%); }

  .brand { position: absolute; text-align: center; color: var(--ink); font-weight: 700; line-height: 1.1; }
  .brand-dot { display: block; margin: 0 auto 14px; border-radius: 50%; background: var(--brand); }

  .flyer-info .brand { left: 340px; top: 46px; width: 206px; font-size: 22px; }
  .flyer-info .brand-dot { width: 60px; height: 60px; }

  .mission-box {
    position: absolute; left: 307px; top: 222px; width: 281px; height: 126px;
    border-radius: 8px 0 0 0;
    background: linear-gradient(90deg, var(--brand-deep), var(--brand-bright) 55%, var(--brand-deep));
    color: #fff; font-weight: 600; font-size: 15.5px; line-height: 20.5px;
    padding: 18px 14px 0 34px;
  }

  .copy { position: absolute; font-size: 10.2px; line-height: 15.9px; color: var(--body); }
  .copy strong { color: var(--ink); }
  .copy .hl { color: var(--brand-deep); font-weight: 700; font-size: 11.6px; }
  .copy-main { left: 345px; top: 362px; width: 228px; }
  .copy-aside { left: 345px; top: 585px; width: 228px; color: var(--accent-sky); font-weight: 700; font-size: 11.2px; line-height: 16px; }
  .copy-invite { left: 18px; top: 578px; width: 296px; }

  .email-band {
    position: absolute; left: 0; bottom: 0; width: 100%; height: 56px;
    background: linear-gradient(90deg, var(--brand-deep), var(--brand-bright) 55%, var(--brand-deep));
    color: #fff; font-weight: 600; font-size: 20px;
    display: flex; align-items: center; padding-left: 95px;
  }

  /* event flyer */
  .flyer-event .brand { left: 22px; top: 45px; width: 170px; font-size: 17px; }
  .flyer-event .brand-dot { width: 50px; height: 50px; margin-bottom: 10px; }

  .headline { position: absolute; font-family: "Oswald", sans-serif; font-weight: 700; color: var(--brand-deep); text-transform: uppercase; line-height: 1; letter-spacing: -1px; }
  .headline-big { left: 62px; top: 222px; font-size: 96px; }
  .headline-talent { left: 258px; top: 244px; font-size: 64px; }
  .headline-search { left: 200px; top: 312px; font-size: 66px; }

  .mission-line { position: absolute; left: 203px; top: 388px; width: 220px; font-family: "Oswald", sans-serif; font-weight: 500; font-size: 13.6px; line-height: 17px; color: var(--brand-deep); letter-spacing: -.4px; }
  .event-copy { position: absolute; left: 203px; top: 449px; width: 236px; font-size: 9.4px; line-height: 14.2px; color: var(--body); }

  .date-pill {
    position: absolute; left: 129px; top: 515px; width: 308px; height: 52px;
    border-radius: 10px;
    background: linear-gradient(90deg, var(--brand-deep), var(--brand-bright) 60%, var(--brand-deep));
    color: #fff; font-weight: 700; font-size: 10.4px; line-height: 16px;
    padding: 10px 0 0 74px;
  }
  .reserve { position: absolute; left: 203px; top: 588px; font-size: 9.4px; font-weight: 700; color: #333; }
  .event-email { position: absolute; left: 203px; top: 605px; font-size: 10.6px; font-weight: 700; color: var(--brand-deep); letter-spacing: -.1px; }
</style>
</head>
<body>

<section class="flyer flyer-info">
  <div class="backdrop"></div>
  <div class="photo" style="left:150px; top:45px; width:185px; height:470px;" role="img" aria-label="Boy in red shirt playing an electric guitar"></div>
  <div class="photo photo-girl" style="left:8px; top:195px; width:200px; height:370px;" role="img" aria-label="Girl in blue striped top dancing"></div>

  <div class="brand"><span class="brand-dot"></span>Harbor Sprouts<br>Star Agency</div>

  <div class="mission-box">Harbor Sprouts Star Agency’s mission is to give military children equal access to participate in the entertainment industry.</div>

  <p class="copy copy-main">Are you an active duty military parent that is constantly pcs and finds it difficult to <span class="hl">help your child find entertainment industry opportunities</span>? Or a retired veteran transitioning or transitioned out of the military that has no idea where to start the journey to support your child’s endeavors? Do you have a child with a talent (<strong>sing, dance, acting or special skill</strong>)? Do you see your child in the mirror pretending to be a star? Does your child have a heart to give back to society through volunteerism?</p>

  <p class="copy copy-aside">Looking for brats that are not only talented but brats that desire to give back to society, as volunteerism is important to Harbor Sprouts Star Agency.</p>

  <p class="copy copy-invite">Harbor Sprouts Star Agency is looking for talent – girl and boy brats ages 5 – 17. If this sounds like your military brat, HSSA invites military parents to submit a head shot and short summary describing your child (name, age, talent, charity and parent’s military branch of service to our email address below.</p>

  <div class="email-band">sprouts@harborsproutsstaragency.com</div>
</section>

<section class="flyer flyer-event">
  <div class="backdrop"></div>
  <div class="photo" style="left:205px; top:15px; width:248px; height:362px;" role="img" aria-label="Boy in red shirt playing an electric guitar"></div>
  <div class="photo photo-girl" style="left:21px; top:297px; width:168px; height:324px;" role="img" aria-label="Girl in blue striped top dancing"></div>

  <div class="brand"><span class="brand-dot"></span>Harbor Sprouts<br>Star Agency</div>

  <h1 class="headline headline-big">Brat</h1>
  <div class="headline headline-talent">Talent</div>
  <div class="headline headline-search">Search</div>

  <p class="mission-line">Harbor Sprouts Star Agency’s mission is to give military children equal access to participate in the entertainment industry.</p>

  <p class="event-copy">Harbor Sprouts Star Agency is looking for talent – girl and boy brats ages 5 – 17. with a talent (sing, dance, acting or special skill) and desire to give back to society, as volunteerism.</p>

  <div class="date-pill">WASHINGTON, D.C. ON MARCH 25, 2017<br>MARCH 25, 2017, 10 AM – 2 PM</div>

  <p class="reserve">RESERVE YOUR SPACE NOW, LIMITED SPOTS!</p>
  <p class="event-email">sprouts@harborsproutsstaragency.com</p>
</section>

</body>
</html>
```